Breakfast Menu at a Bar and Grill

6" x 9" flyer
The attached powerpoint file contains slides with the text to be included in the front and back of the flyer. I will leave it to the designer to suggest color and background designs. Marlowe's Quiet Corner is a no frills dive bar with a blue color customer base. A simple breakfast theme will do.

Target Market(s)

Seniors and blue collar workers.

Font styles to use
Decorative

Colors

Designer to choose colors to be used in the design.

Requirements
Must have
• Our Logo (attached jpg) and the text in the attached PowerPoint file. Some kind of breakfast dish as the background. I will rely on the designers regards the font sizes.
Nice to have
• The background design should have a pic of a breakfast plate that matches one of the items on special...perhaps two pics?
Should not have
• pic that shows food that is not listed on the flyer.

```html
<!DOCTYPE html>
<html lang="en">
<head>
<meta charset="utf-8">
<title>Marlowe's Quiet Corner – Breakfast Specials Flyer</title>
<link href="https://fonts.googleapis.com/css2?family=Oswald:wght@400;500;600;700&family=Open+Sans:wght@400;600&display=swap" rel="stylesheet">
<style>
  :root{
    --red:#e8322b;
    --red-deep:#d42a24;
    --orange:#f3602c;
    --ink:#161616;
    --charcoal:#262626;
    --paper:#ebebeb;
    --stage:#dcdcdc;
    --white:#ffffff;
    --text-dark:#333333;
  }
  *{margin:0;padding:0;box-sizing:border-box}
  html,body{width:1200px;height:903px;overflow:hidden;background:var(--stage)}
  .canvas{position:relative;width:1200px;height:903px}
  .flyer{position:absolute;top:99px;width:470px;height:705px;overflow:hidden;
    box-shadow:0 6px 18px rgba(0,0,0,.25)}
  .flyer--front{left:80px;background:linear-gradient(180deg,#2a2a2a 0%,#1a1a1a 45%,#121212 100%)}
  .flyer--back{left:650px;background:var(--paper)}
  .bands{position:absolute;left:0;width:470px}
  .bands--top{top:0;height:100px}
  .bands--bottom{bottom:0;height:160px}

  .brand-name{font-family:'Oswald',sans-serif;font-weight:600;color:var(--white);
    text-align:center;text-transform:uppercase;letter-spacing:1px}
  .flyer--front .brand-name{position:absolute;top:120px;left:0;width:100%;font-size:34px;line-height:40px}

  .offer{position:absolute;top:208px;left:15px;width:440px;font-family:'Open Sans',sans-serif;
    font-size:11px;line-height:16px;color:var(--white);text-align:center}

  .photo--hero{position:absolute;top:262px;left:0;width:470px;height:300px;
    background:radial-gradient(ellipse at 50% 55%,#d9a866 0%,#a8663a 35%,#4b2d1c 65%,#1c1c1c 100%)}
  .hero-tag{position:absolute;top:500px;right:0;width:175px;height:34px;background:rgba(60,60,60,.85);
    font-family:'Oswald',sans-serif;font-weight:500;font-size:15px;color:var(--white);
    text-align:center;line-height:34px;text-transform:uppercase;white-space:nowrap}

  .hours{position:absolute;bottom:0;width:136px;height:118px;color:var(--white);
    font-family:'Oswald',sans-serif;font-weight:500;font-size:14.5px;line-height:24px;text-align:center;
    padding-top:30px;text-transform:uppercase}
  .hours svg{position:absolute;top:0;left:0}
  .hours span{position:relative;display:block}
  .flyer--front .hours{left:18px}
  .flyer--back .hours{left:11px}

  .contact{position:absolute;right:22px;bottom:12px;text-align:right;font-family:'Open Sans',sans-serif;
    font-style:normal;font-size:13.5px;line-height:18px;color:var(--white)}
  .contact .social{display:inline-block;width:18px;height:18px;border:1.5px solid var(--white);
    border-radius:50%;margin-bottom:8px}

  /* back */
  .side-column{position:absolute;top:0;left:11px;width:211px;height:705px;background:var(--ink)}
  .brand-panel{position:absolute;top:0;left:18px;width:196px;height:128px;background:var(--red);
    box-shadow:0 4px 8px rgba(0,0,0,.4);display:flex;align-items:center;justify-content:center}
  .brand-panel .brand-name{font-size:24px;line-height:28px;padding:0 12px}
  .dish{position:absolute;left:18px;width:194px;height:130px;border:3px solid var(--white);
    box-shadow:0 2px 6px rgba(0,0,0,.4)}
  .dish--skillet{top:149px;background:radial-gradient(circle at 50% 50%,#e4572e 0%,#f0a24a 35%,#6a7a3a 65%,#4a4a44 100%)}
  .dish--omelet{top:301px;background:radial-gradient(ellipse at 50% 55%,#e8c26a 0%,#c98a3e 40%,#efefe8 70%,#b8b8b0 100%)}
  .dish--drink{top:448px;background:radial-gradient(circle at 45% 50%,#f3a46a 0%,#e36a2a 30%,#3a2a22 65%,#111 100%)}

  .menu-title{position:absolute;top:0;left:232px;width:228px;font-family:'Oswald',sans-serif;
    font-weight:700;font-size:82px;line-height:92px;color:var(--red);text-align:center;letter-spacing:3px}
  .ribbon{position:absolute;top:82px;left:232px;width:227px;height:24px}
  .ribbon span{position:absolute;inset:0;font-family:'Oswald',sans-serif;font-weight:500;font-size:13.5px;
    line-height:24px;color:var(--white);text-align:center;letter-spacing:1px}

  .menu-section{position:absolute;left:229px;width:230px}
  .menu-section h2{height:21px;background:var(--red);
    clip-path:polygon(2% 10%,98% 0,100% 50%,97% 100%,1% 92%,0 45%);
    font-family:'Oswald',sans-serif;font-weight:600;font-size:13.5px;line-height:21px;
    color:var(--white);text-align:center;text-transform:uppercase;letter-spacing:.5px}
  .menu-list{list-style:none;margin-top:16px;padding:0 20px 0 4px}
  .menu-item{display:flex;align-items:baseline;font-family:'Open Sans',sans-serif;font-size:10px;
    line-height:16.3px;color:var(--text-dark);text-transform:uppercase}
  .menu-item .leader{flex:1;border-bottom:1px dotted #888;margin:0 4px;transform:translateY(-3px)}
  .menu-item .price{font-weight:600}
  .menu-section--traditional{top:135px}
  .menu-section--omelets{top:285px}
  .menu-section--drinks{top:430px}
</style>
</head>
<body>
<main class="canvas">

  <section class="flyer flyer--front">
    <svg class="bands bands--top" viewBox="0 0 470 100" aria-hidden="true">
      <polygon points="0,0 470,0 470,14 0,88" fill="var(--red)"/>
      <polygon points="0,70 470,4 470,18 0,86" fill="var(--orange)"/>
    </svg>
    <h1 class="brand-name">Marlowe's Quiet Corner</h1>
    <p class="offer">Free Breakfast on Sunday with a two drink purchase.&nbsp; Monday through Saturday;<br>Purchase a breakfast special item with a two drink minimum and get one free.</p>
    <div class="photo--hero" role="img" aria-label="Stack of pancakes layered with crispy bacon and syrup on a white plate"></div>
    <div class="hero-tag">Marlowe's Quiet Corner</div>
    <svg class="bands bands--bottom" viewBox="0 0 470 160" aria-hidden="true">
      <polygon points="0,58 470,2 470,18 0,74" fill="var(--orange)"/>
      <polygon points="0,70 470,14 470,160 0,160" fill="var(--red)"/>
      <polygon points="0,110 470,60 470,160 0,160" fill="var(--red-deep)"/>
    </svg>
    <div class="hours">
      <svg width="136" height="118" viewBox="0 0 136 118" aria-hidden="true">
        <polygon points="0,0 68,16 136,0 136,118 0,118" fill="var(--ink)"/>
      </svg>
      <span>Breakfast Specials</span><span>6AM – 11AM</span><span>7 Days a Week</span>
    </div>
    <address class="contact">
      <span class="social" aria-hidden="true"></span><br>
      Tel: 602-555-0142<br>
      4810 N. Dusty Mesa Rd. Phoenix, Az 85032<br>
      www.marlowesquietcorner.com
    </address>
  </section>

  <section class="flyer flyer--back">
    <div class="side-column"></div>
    <div class="brand-panel"><span class="brand-name">Marlowe's Quiet Corner</span></div>
    <div class="dish dish--skillet" role="img" aria-label="Skillet of scrambled eggs with peppers and vegetables"></div>
    <div class="dish dish--omelet" role="img" aria-label="Folded omelet with bacon bits and toast on a plate"></div>
    <div class="dish dish--drink" role="img" aria-label="Screwdriver cocktail with orange slices"></div>

    <h1 class="menu-title">MENU</h1>
    <div class="ribbon">
      <svg width="227" height="24" viewBox="0 0 227 24" aria-hidden="true">
        <polygon points="0,0 227,0 219,12 227,24 0,24 8,12" fill="var(--red)"/>
      </svg>
      <span>BREAKFAST SPECIALS</span>
    </div>

    <div class="menu-section menu-section--traditional">
      <h2>Traditional Favorites</h2>
      <ul class="menu-list">
        <li class="menu-item"><span>The 5-Star Breakfast</span><span class="leader"></span><span class="price">$5.50</span></li>
        <li class="menu-item"><span>Pancakes w/Bacon</span><span class="leader"></span><span class="price">$5.50</span></li>
        <li class="menu-item"><span>2 Eggs Bacon or Sausage</span><span class="leader"></span><span class="price">$5.50</span></li>
        <li class="menu-item"><span>3 Pancakes</span><span class="leader"></span><span class="price">$4.00</span></li>
        <li class="menu-item"><span>3 French Toast</span><span class="leader"></span><span class="price">$4.00</span></li>
      </ul>
    </div>

    <div class="menu-section menu-section--omelets">
      <h2>Omelets</h2>
      <ul class="menu-list">
        <li class="menu-item"><span>California Omelet</span><span class="leader"></span><span class="price">$6.00</span></li>
        <li class="menu-item"><span>Green Chili Omelet</span><span class="leader"></span><span class="price">$6.00</span></li>
        <li class="menu-item"><span>Pueblo Omelet</span><span class="leader"></span><span class="price">$6.00</span></li>
        <li class="menu-item"><span>Spanish Omelet</span><span class="leader"></span><span class="price">$6.00</span></li>
        <li class="menu-item"><span>Basic Breakfast Omelet</span><span class="leader"></span><span class="price">$6.00</span></li>
      </ul>
    </div>

    <div class="menu-section menu-section--drinks">
      <h2>Drink Specials</h2>
      <ul class="menu-list">
        <li class="menu-item"><span>Domestic Bottles</span><span class="leader"></span><span class="price">$1.75</span></li>
        <li class="menu-item"><span>Domestic Drafts</span><span class="leader"></span><span class="price">$2.00</span></li>
        <li class="menu-item"><span>Well Drinks</span><span class="leader"></span><span class="price">$3.00</span></li>
        <li class="menu-item"><span>Screwdrivers</span><span class="leader"></span><span class="price">$3.00</span></li>
      </ul>
    </div>

    <svg class="bands bands--bottom" viewBox="0 0 470 160" aria-hidden="true">
      <polygon points="0,58 470,2 470,18 0,74" fill="var(--orange)"/>
      <polygon points="0,70 470,14 470,160 0,160" fill="var(--red)"/>
      <polygon points="0,110 470,60 470,160 0,160" fill="var(--red-deep)"/>
    </svg>
    <div class="hours">
      <svg width="136" height="118" viewBox="0 0 136 118" aria-hidden="true">
        <polygon points="0,0 68,16 136,0 136,118 0,118" fill="var(--ink)"/>
      </svg>
      <span>Breakfast Specials</span><span>6AM – 11AM</span><span>7 Days a Week</span>
    </div>
    <address class="contact">
      <span class="social" aria-hidden="true"></span><br>
      Tel: 602-555-0142<br>
      4810 N. Dusty Mesa Rd. Phoenix, Az 85032<br>
      www.marlowesquietcorner.com
    </address>
  </section>

</main>
</body>
</html>
```